依頼詳細
当サイトに店舗情報等を掲載してもらうための店舗への説明用チラシのデザイン制作をお願い致します。思わず掲載をしたくなるようなデザインをお願いします。シンプルでわかり易いものが希望です。
記載項目
サイト名はsemu(セム)・店舗情報掲載料1P21,000円/年額 複数P(写真・メニュー・クーポン等)42,000円/年額 求人情報掲載無料・採用時31,500円 当サイトの収益は児童養護施設等の子供達の学習支援に使われます。
サイズ
A4
ページ数
片面
希望イメージ
シンプル 複雑
単色 カラフル
暗い 明るい
日常 高級
遊び心 厳粛
未来的 伝統的
女性的 男性的
希望する色
オレンジ
納品ファイル
• 高解像度JPG (.jpg)
• イラストレーター形式 (.ai)
補足説明
《選ぶワクワクを全ての人に》をミッションにしたNPOです。この度開設するサイトを通じて、大人の生活の選択肢を増やし、学習支援によって子どもの将来の選択肢を増やすことを目的としています。サイト開設にあたっては、一定数の店舗登録が必須なため、店舗への説明がわかりやすい営業用チラシが必要です。イメージとしてはひらけ堂やぽみたすが近いかと思います。

```html
<!DOCTYPE html>
<html lang="ja">
<head>
<meta charset="utf-8">
<title>SEMU 店舗掲載のご案内</title>
<link rel="stylesheet" href="https://fonts.googleapis.com/css2?family=M+PLUS+Rounded+1c:wght@400;700;800&family=Kosugi+Maru&display=swap">
<style>
:root{
  --orange:#f39a1e;
  --orange-deep:#e67e0a;
  --white:#ffffff;
  --ink:#3a2a1a;
  --cream:#fff6e6;
  --shot-top:#f6e7c9;
  --shot-bottom:#d9a566;
}
*{box-sizing:border-box;margin:0;padding:0}
html,body{width:849px;height:1200px;overflow:hidden}
body{background:var(--orange);font-family:"M PLUS Rounded 1c",sans-serif;color:var(--ink)}
.flyer{position:relative;width:849px;height:1200px;overflow:hidden}
.tagline{position:absolute;left:30px;top:26px;color:var(--white);font-size:19px;font-weight:700;letter-spacing:1px}
.title-block{position:absolute;left:22px;top:48px;display:flex;align-items:flex-start;gap:14px}
.site-name{color:var(--white);font-weight:800;font-size:150px;letter-spacing:4px;line-height:1}
.site-kana{color:var(--white);font-weight:800;font-size:42px;writing-mode:vertical-rl;letter-spacing:4px;line-height:1;margin-top:14px}
.open-badge{position:absolute;left:650px;top:60px;width:175px;height:100px;background:var(--white);color:var(--orange);text-align:center;font-weight:800;font-size:34px;line-height:44px;padding-top:6px}
.banner{position:absolute;left:0;top:205px;width:849px;height:34px;background:var(--white);font-weight:700;font-size:19px;line-height:34px;padding-left:30px}
.site-preview{position:absolute;left:215px;top:265px;width:420px;height:460px;background:linear-gradient(180deg,var(--shot-top),var(--cream) 40%,var(--shot-bottom));border:6px solid var(--white);box-shadow:0 3px 10px rgba(0,0,0,.18)}
.voice{position:absolute;writing-mode:vertical-rl;color:var(--white);font-family:"Kosugi Maru",sans-serif;font-size:22px;letter-spacing:3px}
.voice.small{font-size:18px}
.v1{left:150px;top:300px}
.v2{left:120px;top:395px;font-size:26px}
.v3{left:160px;top:520px}
.v4{left:690px;top:290px}
.v5{left:655px;top:400px}
.v7{left:680px;top:600px}
.fees{position:absolute;left:18px;top:790px;width:410px}
.fees-title{background:var(--white);color:var(--orange);font-weight:800;font-size:20px;padding:6px 12px;width:210px;margin-bottom:8px}
.fee-row{display:flex;height:62px;margin-bottom:8px}
.fee-label{width:90px;background:var(--cream);border:2px solid var(--white);display:flex;flex-direction:column;justify-content:center;align-items:center;font-weight:700;font-size:17px;color:var(--orange-deep);text-align:center;line-height:1.2}
.fee-label small{font-size:10px;color:var(--ink)}
.fee-value{flex:1;background:var(--white);display:flex;align-items:center;padding-left:20px;font-weight:800;font-size:24px;color:var(--ink)}
.fee-value small{font-size:15px;font-weight:700;margin-left:4px}
.contact{background:var(--white);margin-top:4px;padding:10px 14px;font-weight:700;font-size:17px}
.about{position:absolute;left:450px;top:830px;width:378px;height:290px;background:var(--white)}
.about-title{background:var(--orange-deep);color:var(--white);font-weight:800;font-size:22px;padding:8px 16px}
.about-body{padding:14px 18px;font-size:14px;line-height:1.85}
</style>
</head>
<body>
<div class="flyer">
  <p class="tagline">熊本県八代市の地域情報ポータルサイト</p>
  <div class="title-block">
    <h1 class="site-name">SEMU</h1>
    <span class="site-kana">セム</span>
  </div>
  <div class="open-badge">2014年<br>OPEN</div>
  <p class="banner">地域のイベント情報や店舗情報等様々なコンテンツを掲載</p>

  <div class="site-preview" role="img" aria-label="セムのウェブサイト画面イメージ(料理写真やランキング、記事一覧)"></div>

  <span class="voice small v1">この求人気になる</span>
  <span class="voice v2">ワクワク</span>
  <span class="voice small v3">あの店の新作出てる?</span>
  <span class="voice small v4">晩ご飯はこのレシピが良いかな?</span>
  <span class="voice v5">ワクワク</span>
  <span class="voice small v7">週末はあそこに行こう</span>

  <section class="fees">
    <h2 class="fees-title">店舗情報掲載料</h2>
    <div class="fee-row"><div class="fee-label">1P</div><div class="fee-value">21,000円<small>/年額</small></div></div>
    <div class="fee-row"><div class="fee-label">複数P<small>写真・メニュー・クーポン等</small></div><div class="fee-value">42,000円<small>/年額</small></div></div>
    <div class="fee-row"><div class="fee-label">求人情報<br>掲載</div><div class="fee-value">無料<small>(採用時31,500円)</small></div></div>
    <p class="contact">お問い合わせは 012-345-6789(担当:××)まで</p>
  </section>

  <section class="about">
    <h2 class="about-title">What's セム?</h2>
    <p class="about-body">セムは《選ぶワクワクを全ての人に》をミッションにしたNPOです。当サイトの収益は児童養護施設等の子供達の学習支援に使われます。この活動は、大人の生活の選択肢を増やし、学習支援によって子どもの将来の選択肢を増やすことを目的としています。</p>
  </section>
</div>
</body>
</html>
```